Velvo Leaf needs a luxury packaging design

I'm starting a tea brand from the ground up. The working name as of now is Velvo Leaf. I intend for it to be a luxury loose leaf tea brand.

I want the aesthetic of it to be luxurious in nature. The color schemes that I am liking right now include black, gold, silver, rose gold and anything along that luxury feel line. One of the things I love most is UNIQUE packaging of the tea itself. I'll attach inspiration below.

I want the consumer every single time they use this product to feel like it is an experience. The person I choose will also be the person I consider for all further needs on a design basis moving forward if they would like to continue to work with me.

This is a really great opportunity to work with a luxury line that also does social good as some proceeds from each purchase will go to a mental health awareness cause.

The key is for the packaging to represent luxury, give off a unique feel that gets the consumer excited to see it and show it off to their peers on social media

Target Market(s)

The Modern Millenial, 21-40 (bullseye 28). He or she is a young professional that has a disposable income in which they do like to indulge with. They balance their demanding work schedules well and they have a work hard/play hard mindset. This professional is more likely to order their daily coffee from Brewhaven as opposed to Gus Pellery and their social media profiles are a big indicator as to their hobbies and lifestyles outside of their work environment. They enjoy shopping at stores like Ondi, Valkorn, Fenwire/FenMan and for special occasions are willing to splurge at stores like Marlow's, Maison Verdal and… They live a pretty active lifestyle and are highly influenced by social media trending products

Requirements
Must have
• Luxurious, must have exclusive look
Nice to have
• unique packaging
• viral inspired design
Should not have
• brown color, childish feel, bubble letters

```html
<!DOCTYPE html>
<html lang="en">
<head>
<meta charset="UTF-8">
<title>Velvo Leaf – Packaging Panel</title>
<link rel="stylesheet" href="https://fonts.googleapis.com/css2?family=Gentium+Book+Plus:wght@700&display=swap">
<style>
  :root {
    --page-bg: #ffffff;
    --rule-green: #4a8a1f;
    --panel-black: #030303;
    --grid-line: rgba(255, 255, 255, 0.07);
    --gold: #b89a4e;
    --gold-light: #f0dc7a;
    --gold-mid: #c9a23c;
    --gold-deep: #8a5a22;
    --ink: #111111;
  }
  * { margin: 0; padding: 0; box-sizing: border-box; }
  html, body {
    width: 1200px;
    height: 903px;
    overflow: hidden;
    background: var(--page-bg);
  }
  .page {
    position: relative;
    width: 1200px;
    height: 903px;
    background: var(--page-bg);
  }
  .page-rule {
    position: absolute;
    left: 0;
    width: 1200px;
    height: 4px;
    background: var(--rule-green);
  }
  .page-rule--top { top: 0; }
  .page-rule--bottom { bottom: 0; }

  .package-panel {
    position: absolute;
    left: 180px;
    top: 102px;
    width: 833px;
    height: 625px;
    overflow: hidden;
    background-color: var(--panel-black);
    background-image:
      repeating-linear-gradient(90deg, transparent 0 38px, var(--grid-line) 38px 40px, transparent 40px 52px, var(--grid-line) 52px 53px),
      repeating-linear-gradient(0deg, transparent 0 38px, var(--grid-line) 38px 40px, transparent 40px 52px, var(--grid-line) 52px 53px);
    box-shadow: 2px 2px 3px rgba(0, 0, 0, 0.35);
  }

  .border-band { position: absolute; top: 0; height: 100%; }
  .border-line {
    position: absolute;
    top: 0;
    height: 100%;
    background: linear-gradient(90deg, var(--gold-deep), var(--gold-light), var(--gold-mid));
  }
  .border-line--outer { left: 11px; width: 5px; }
  .border-line--inner-left { left: 40px; width: 2px; }
  .border-line--inner-right { left: 158px; width: 2px; }
  .border-line--edge { left: 177px; width: 5px; }
  .border-ornament {
    position: absolute;
    top: 0;
    left: 45px;
    width: 110px;
    height: 100%;
    background: linear-gradient(90deg, #6b4f1c, #d8bb5c 30%, #a88234 60%, #e6cf72 85%, #6b4f1c);
    opacity: 0.85;
  }

  .swirl-art {
    position: absolute;
    border-radius: 50%;
  }
  .swirl-art--right {
    left: 500px;
    top: -80px;
    width: 420px;
    height: 800px;
    background: radial-gradient(ellipse at 55% 50%, rgba(240, 220, 122, 0.55), rgba(201, 162, 60, 0.45) 35%, rgba(138, 90, 34, 0.35) 60%, rgba(0, 0, 0, 0) 75%);
  }
  .swirl-art--lower {
    left: 250px;
    top: 430px;
    width: 330px;
    height: 300px;
    background: radial-gradient(ellipse at 70% 80%, rgba(201, 162, 60, 0.45), rgba(138, 90, 34, 0.25) 45%, rgba(0, 0, 0, 0) 70%);
  }

  .label-tab {
    position: absolute;
    display: flex;
    align-items: center;
    justify-content: center;
    background: var(--gold);
    color: var(--ink);
    font-family: "Gentium Book Plus", Georgia, serif;
    font-weight: 700;
    font-size: 31px;
    white-space: nowrap;
  }
  .label-tab--tagline {
    left: 243px;
    top: 0;
    width: 242px;
    height: 61px;
    border-radius: 0 0 14px 14px;
  }
  .label-tab--brand {
    right: 0;
    top: 433px;
    width: 170px;
    height: 60px;
    border-radius: 12px 0 0 12px;
  }
</style>
</head>
<body>
  <div class="page">
    <div class="page-rule page-rule--top"></div>

    <section class="package-panel">
      <div class="border-band">
        <div class="border-line border-line--outer"></div>
        <div class="border-line border-line--inner-left"></div>
        <div class="border-ornament" role="img" aria-label="Vertical gold ornamental border of fan and scroll motifs"></div>
        <div class="border-line border-line--inner-right"></div>
        <div class="border-line border-line--edge"></div>
      </div>

      <div class="swirl-art swirl-art--right" role="img" aria-label="Sweeping gold and bronze ribbon swirls"></div>
      <div class="swirl-art swirl-art--lower" role="img" aria-label="Fine gold flourish lines rising from the lower edge"></div>

      <div class="label-tab label-tab--tagline">Quality Tea</div>
      <div class="label-tab label-tab--brand">Velvo Leaf</div>
    </section>

    <div class="page-rule page-rule--bottom"></div>
  </div>
</body>
</html>
```